Looking for a professional, clean and crisp business card

I am in the underground utilities industry and am just looking for a really impressive business card. I would like our card to be white with our symbol crisp and clear with it protruding. I also have a business partner that will require his name and info on the card once the design is set. I would like to have our website info on the card which is;
http://granitetrenchco.example/

Contact Information for Business Card

Website, contact name, number and email

```html
<!DOCTYPE html>
<html lang="en">
<head>
<meta charset="utf-8">
<title>Granite Trench Co – Business Card</title>
<link rel="stylesheet" href="https://fonts.googleapis.com/css2?family=Roboto:wght@400;700;900&display=swap">
<style>
  :root {
    --backdrop: #e9e6e2;
    --card-black: #111112;
    --card-white: #ffffff;
    --brand-blue: #3a5eab;
    --brand-red: #e3202b;
    --text-light: #f2f2f2;
    --text-dark: #141414;
  }
  * { margin: 0; padding: 0; box-sizing: border-box; }
  html, body {
    width: 1200px; height: 909px; overflow: hidden;
    background: var(--backdrop);
    font-family: "Roboto", Arial, sans-serif;
  }
  .sheet {
    position: relative; width: 1200px; height: 909px;
    display: flex; flex-direction: column; align-items: center; justify-content: center; gap: 50px;
  }
  .card {
    position: relative; width: 630px; height: 360px; border-radius: 22px; overflow: hidden;
    box-shadow: 0 6px 18px rgba(0,0,0,0.18);
  }
  .card--front { background: var(--card-black); display: flex; align-items: center; justify-content: center; }
  .card--back { background: var(--card-white); }
  .brand-mark { display: flex; align-items: center; gap: 14px; }
  .brand-mark__dot { width: 26px; height: 26px; border-radius: 50%; }
  .brand-mark__name { font-weight: 900; text-transform: uppercase; letter-spacing: 1px; }
  .card--front .brand-mark__dot { background: var(--brand-blue); }
  .card--front .brand-mark__name { color: var(--card-white); font-size: 36px; }
  .card--back .brand-mark { position: absolute; left: 40px; top: 150px; }
  .card--back .brand-mark__dot { background: var(--text-dark); width: 20px; height: 20px; }
  .card--back .brand-mark__name { color: var(--text-dark); font-size: 24px; }
  .swoosh { position: absolute; inset: 0; width: 630px; height: 360px; }
  .person { position: absolute; right: 40px; top: 26px; text-align: right; }
  .person__name { color: var(--brand-blue); font-weight: 700; font-size: 30px; line-height: 1.1; }
  .person__title { color: var(--brand-red); font-size: 17px; line-height: 1.3; }
  .contact { position: absolute; right: 34px; top: 178px; text-align: right; color: var(--text-light); font-size: 14.5px; line-height: 1.4; }
  .contact__address { margin-bottom: 10px; }
  .contact__line { display: flex; justify-content: flex-end; align-items: center; gap: 9px; }
  .contact__icon { width: 13px; height: 13px; flex: none; }
  .contact__icon * { fill: var(--brand-red); }
</style>
</head>
<body>
<main class="sheet">
  <section class="card card--front" aria-label="Card front">
    <div class="brand-mark">
      <span class="brand-mark__dot"></span>
      <span class="brand-mark__name">Granite Trench Co</span>
    </div>
  </section>

  <section class="card card--back" aria-label="Card back">
    <svg class="swoosh" viewBox="0 0 630 360" aria-hidden="true">
      <path class="swoosh__stripe swoosh__stripe--red" d="M0,305 C240,300 318,246 380,170 C430,115 480,102 560,112" fill="none" stroke="var(--brand-red)" stroke-width="8"/>
      <path class="swoosh__stripe swoosh__stripe--blue" d="M0,322 C250,318 330,262 395,182 C440,128 485,115 545,122" fill="none" stroke="var(--brand-blue)" stroke-width="7"/>
      <path class="swoosh__panel" d="M150,360 C330,330 385,240 430,175 C475,115 540,102 630,100 L630,360 Z" fill="var(--card-black)"/>
    </svg>

    <div class="brand-mark">
      <span class="brand-mark__dot"></span>
      <span class="brand-mark__name">Granite Trench Co</span>
    </div>

    <div class="person">
      <div class="person__name">Dorian Keller</div>
      <div class="person__title">Owner/CEO</div>
    </div>

    <div class="contact">
      <div class="contact__address">418 W Quarry Road<br>Maple Ridge County 7402</div>
      <div class="contact__line">555-014-2286
        <svg class="contact__icon" viewBox="0 0 16 16"><path d="M3 1l3 3-2 2c1 2 3 4 5 5l2-2 3 3-2 3C6 14 2 10 1 3z"/></svg>
      </div>
      <div class="contact__line">info@granitetrenchco.example
        <svg class="contact__icon" viewBox="0 0 16 16"><path d="M1 3h14v10H1z M1 3l7 6 7-6" stroke="#111" stroke-width="1"/></svg>
      </div>
      <div class="contact__line">www.granitetrenchco.example
        <svg class="contact__icon" viewBox="0 0 16 16"><circle cx="8" cy="8" r="7"/></svg>
      </div>
    </div>
  </section>
</main>
</body>
</html>
```